Bref créative
Biotech - Stationary, Business Cards, Envelopes
Stationary, Business Cards, Envelopes
Professional
Martin Kessler
President & CEO
718 Larkspur Road Suite 4203
New York, NY 10001
ceo@velmarisco.example
www.velmarisco.example
Back of business card should have the web address in medium size letters written across the middle of the card: "www.velmarisco.example". could also feature a solid color background or some creative design.
HERE IS THE COMPANY LOGO TO BE USED
COMPANY LOGO AI FILE

```html
<!DOCTYPE html>
<html lang="en">
<head>
<meta charset="utf-8">
<title>Velmaris Co Stationery</title>
<link href="https://fonts.googleapis.com/css2?family=Questrial&display=swap" rel="stylesheet">
<style>
:root{
  --bg:#e8e5e1;
  --paper:#ffffff;
  --cyan:#1ba6e2;
  --sky:#5cc6ef;
  --yellow:#f6b90f;
  --ink:#4a4d52;
  --muted:#7d8187;
  --card-dark:#2b2d33;
}
*{margin:0;padding:0;box-sizing:border-box}
html,body{width:1200px;height:864px;overflow:hidden;background:var(--bg)}
body{position:relative;font-family:"Questrial",Arial,sans-serif;color:var(--ink)}
.sheet{position:absolute;background:var(--paper);box-shadow:0 2px 6px rgba(0,0,0,.18)}
.brand{display:flex;align-items:center;gap:8px;color:var(--cyan);white-space:nowrap}
.brand-mark{background:var(--cyan)}

/* Letterhead */
.letterhead{left:48px;top:91px;width:500px;height:713px}
.letterhead .brand{position:absolute;left:28px;top:30px;font-size:30px}
.letterhead .brand-mark{width:22px;height:22px}
.sender{position:absolute;right:26px;top:14px;text-align:right;font-size:9px;line-height:1.45;color:var(--muted)}
.sender .name{font-size:18px;color:var(--cyan);letter-spacing:.5px;line-height:1.2}
.letter{position:absolute;left:28px;top:270px;width:444px;font-size:8.4px;line-height:1.55;color:var(--ink)}
.letter .addressee{margin-bottom:16px}
.letter h2{font-size:10.5px;font-weight:400;color:var(--ink);margin-bottom:4px}
.letter p{margin-bottom:6px}
.signoff{margin-top:6px}
.signature{display:block;width:60px;height:22px;margin:2px 0}
.footer-contact{position:absolute;left:28px;bottom:22px;font-size:7px;line-height:1.5;color:var(--muted)}
.letter-bands{position:absolute;left:0;bottom:0;width:100%;height:12px}
.letter-bands .band-yellow{position:absolute;left:0;bottom:0;width:32%;height:12px;background:var(--yellow)}
.letter-bands .band-cyan{position:absolute;left:30%;bottom:0;right:0;height:5px;background:var(--cyan)}

/* Business cards */
.card{width:212px;height:96px}
.card-back{left:600px;top:91px;background:var(--card-dark);display:flex;align-items:center;justify-content:center}
.card-back .web{color:var(--sky);font-size:14px;letter-spacing:.3px}
.card-front{left:835px;top:91px;overflow:hidden}
.card-front .brand{position:absolute;left:10px;top:12px;font-size:12px;gap:5px}
.card-front .brand-mark{width:9px;height:9px}
.card-front .person{position:absolute;right:10px;top:10px;width:78px;font-size:5px;line-height:1.5;color:var(--muted)}
.card-front .person .name{font-size:7px;color:var(--ink)}
.card-front .details{position:absolute;right:10px;top:40px;width:78px;font-size:4.6px;line-height:1.55;color:var(--muted)}
.card-front .band-yellow{position:absolute;left:0;bottom:0;width:46%;height:7px;background:var(--yellow)}
.card-front .band-cyan{position:absolute;left:40%;right:0;bottom:0;height:4px;background:var(--cyan)}

/* Envelope front */
.envelope-front{left:607px;top:245px;width:439px;height:245px;overflow:hidden}
.envelope-front .brand{position:absolute;left:20px;top:22px;font-size:24px}
.envelope-front .brand-mark{width:18px;height:18px}
.envelope-front .return{position:absolute;left:46px;top:56px;font-size:6.2px;line-height:1.5;color:var(--muted)}
.envelope-front .band-cyan{position:absolute;left:0;right:0;bottom:0;height:14px;background:var(--cyan)}
.envelope-front .band-yellow{position:absolute;left:0;bottom:14px;width:36%;height:7px;background:var(--yellow)}

/* Envelope back */
.envelope-back{left:607px;top:509px;width:439px;height:250px}
.envelope-back svg{display:block}
</style>
</head>
<body>

<section class="sheet letterhead" aria-label="Letterhead">
  <div class="brand"><span class="brand-mark"></span>Velmaris Co</div>
  <div class="sender">
    <div class="name">MARTIN KESSLER</div>
    <div>President &amp; CEO</div>
    <div>Email: ceo@velmarisco.example</div>
    <div>Web address: www.velmarisco.example</div>
  </div>
  <div class="letter">
    <div class="addressee">Clara Whitfield<br>Research Director<br>Portland, OR</div>
    <h2>Regarding the Assay Program</h2>
    <p>Our laboratory team has completed the first review of the assay program and the sample logistics plan for your project. We are pleased to share the results with you and to outline the next steps for the coming quarter. The early data show stable signals across all test panels, and the control groups behaved as expected in every run. Our analysts checked each batch twice and logged all values in the shared record, so your staff can follow every change from intake to final report. We also reviewed storage, labeling and transport, and found that the current process meets the quality targets set at the start of the study.</p>
    <p>Each study will follow the agreed protocol, with weekly reports sent to your office. Our staff will remain available for questions at any stage, and we will adjust the schedule as your needs change over time. In the next phase we plan to widen the sample set, add two new markers and compare results with the prior cohort. Thank you for your continued trust in our work. We look forward to a productive partnership and to sharing more findings soon.</p>
    <div class="signoff">
      Best regards,
      <svg class="signature" viewBox="0 0 70 26" aria-hidden="true"><path d="M4 18 C10 4,14 4,12 16 S22 6,26 14 S34 20,40 10 L48 16 L66 8" fill="none" stroke="#333" stroke-width="1.2"/></svg>
      Martin Kessler<br>President &amp; CEO
    </div>
  </div>
  <div class="footer-contact">
    718 Larkspur Road Suite 4203<br>New York, NY 10001<br>ceo@velmarisco.example<br>Tel: (212) 555-0148
  </div>
  <div class="letter-bands"><span class="band-cyan"></span><span class="band-yellow"></span></div>
</section>

<section class="sheet card card-back" aria-label="Business card back">
  <span class="web">www.velmarisco.example</span>
</section>

<section class="sheet card card-front" aria-label="Business card front">
  <div class="brand"><span class="brand-mark"></span>Velmaris Co</div>
  <div class="person"><div class="name">MARTIN KESSLER</div>President &amp; CEO</div>
  <div class="details">718 Larkspur Road Suite 4203<br>New York, NY 10001<br>Tel: (212) 555-0148<br>ceo@velmarisco.example<br>www.velmarisco.example</div>
  <span class="band-cyan"></span><span class="band-yellow"></span>
</section>

<section class="sheet envelope-front" aria-label="Envelope front">
  <div class="brand"><span class="brand-mark"></span>Velmaris Co</div>
  <div class="return">718 Larkspur Road Suite 4203, New York, NY 10001<br>www.velmarisco.example</div>
  <span class="band-yellow"></span><span class="band-cyan"></span>
</section>

<section class="sheet envelope-back" aria-label="Envelope back">
  <svg width="439" height="250" viewBox="0 0 439 250">
    <rect width="439" height="250" fill="#fff"/>
    <rect width="439" height="42" fill="var(--cyan)"/>
    <path d="M0 42 L219.5 140 L439 42 Z" fill="var(--sky)"/>
    <path d="M0 42 L219.5 140 L439 42" fill="none" stroke="#9fa3a8" stroke-width="1"/>
    <path d="M0 250 L185 140 M439 250 L254 140" fill="none" stroke="#c9ccd0" stroke-width="1"/>
  </svg>
</section>

</body>
</html>
```